Divorce Resource

I would like someone to set up a very basic website using WORDPRESS for me - to be developed significantly at a later stage.

I will run initially only as a landing page for an advertising campaign that directs people to the website where they will be informed that it is still under construction and that I would like their input to ensure that all of the research and written material answers all of the commonly asked questions and those that are a little outside of the norm. It will capture a user name and email address and then direct them to answer a brief survey. For their input, they will receive a copy of the ebook once it is finished if they check the box requesting it.

My aim is to capture the questions of the folk who answer the ad so as to develop the website to meet their needs and expectations.

I need access to the contact database and survey results. I have a logo already that has a solid colour background and three jigsaw pieces in the graphics (see attached file). Id like to be able to integrate the jigsaw pieces into the design of the overall website. ie "putting all the pieces together to see the big picture".

The site is for information on divorce ... eventually, it will have all manner of info, including a blog, forums, a secure member's area, book reviews and sales through rivenmart affiliate marketing and a shopping cart for independent item sales.

I have a domain name registered and hosting with BrightHostly in Australia which does support Wordpress. I would like my site to look and feel original and project a professional, reliable but up to date and modern approach to the overall event of a divorce. It must allow for banner advertising and ppc advertising.

Obviously, people who submit on this project, will be given first option to submit on subsequent development.

I look forward to hearing from you.

Target Market(s)

Anyone who is contemplating, going through or coming out the other side of a divorce or separation in Australia.

Industry/Entity Type

Construction

Requirements
Must have
• A database that collates email and usernames
A survey facility that I can easily amend
Collection and collation of survey results
Use of existing logo and colour scheme

```html
<!DOCTYPE html>
<html lang="en">
<head>
<meta charset="utf-8">
<title>splitguide – taking it one step at a time</title>
<link rel="stylesheet" href="https://fonts.googleapis.com/css2?family=Roboto:wght@300;400;500&family=Oswald:wght@600;700&family=Anton&display=swap">
<style>
:root{
  --teal-deep:#0c4450;
  --teal-main:#1b5a66;
  --teal-mid:#226b78;
  --teal-light:#3a8a96;
  --red-ribbon:#b8200e;
  --red-dark:#7d1408;
  --red-title:#b0161c;
  --orange:#f08a12;
  --orange-light:#ffb347;
  --white:#ffffff;
  --text-soft:#e4f0f2;
  --panel-top:#f4f7f8;
  --panel-bottom:#cfdde1;
  --label:#3a4b50;
  --footer-text:#8fb4bb;
}
*{margin:0;padding:0;box-sizing:border-box}
html,body{width:1087px;height:1200px;overflow:hidden}
body{position:relative;background:var(--teal-main);font-family:"Roboto",Arial,sans-serif;color:var(--white)}
.abs{position:absolute}

.site-header{left:0;top:0;width:1087px;height:172px;background:var(--teal-deep)}
.brand{left:43px;top:72px}
.brand-mark{display:inline-block;width:22px;height:22px;background:var(--teal-light);border-radius:50%;vertical-align:middle;margin-right:7px}
.brand-name{font-size:24px;font-weight:400;color:var(--white);vertical-align:middle}
.brand-tagline{font-size:10px;color:var(--text-soft);margin-top:5px;letter-spacing:.3px}
.search{left:851px;top:62px;width:209px;height:31px;border:2px solid #2b7380;border-radius:8px;background:#0f4b57}
.search span{position:absolute;left:12px;top:6px;font-size:14px;color:#8fb4bb}
.search svg{position:absolute;right:8px;top:3px}

.nav{left:0;top:124px;width:1087px;height:44px}
.nav a{position:absolute;top:12px;font-size:14.5px;color:var(--white);text-decoration:none;white-space:nowrap}
.nav .active{left:84px;top:1px;width:77px;height:40px;background:#145661;border:1px solid #3b8793;padding-top:11px;text-align:center}

.hero{left:0;top:172px;width:1087px;height:474px;background:radial-gradient(ellipse at 55% 40%,#3b8a95 0%,#1f6470 55%,#124b56 100%);overflow:hidden}
.hero-devices{left:30px;top:35px;width:400px;height:423px;border-radius:14px;background:linear-gradient(160deg,#5a5e60,#2a2c2d 70%,#7aa63a)}
.hero-reader{left:560px;top:0;width:527px;height:474px;background:linear-gradient(120deg,rgba(31,100,112,0) 0%,#3b3560 45%,#2b2a45 100%)}
.hero-title{left:451px;top:46px;width:360px;font-family:"Oswald",Impact,sans-serif;font-weight:700;font-size:37px;line-height:44px;color:var(--white)}
.hero-text{left:451px;top:140px;width:360px;font-size:14.5px;line-height:26px;font-weight:300;color:var(--white)}
.dots{left:533px;top:442px}
.dots i{display:inline-block;width:11px;height:11px;border-radius:50%;margin-right:3px;background:var(--orange)}
.dots i.on{background:#d8e4e6}
.hero-shadow{left:0;top:646px;width:1087px;height:34px;background:linear-gradient(#072d35,var(--teal-main))}

.welcome-title{left:33px;top:700px;font-size:26px;font-weight:400}
.survey-link{left:39px;top:742px;font-size:17px;color:var(--orange)}
.ebook-cover{left:58px;top:780px;width:172px;height:220px;background:linear-gradient(135deg,#2a2a2a,#111 60%,#6b1010);border-radius:3px}
.new-badge{left:47px;top:952px;width:74px;height:74px;border-radius:50%;background:#1e8fd0;font-size:15px;font-weight:500;text-align:center;line-height:74px}
.intro{left:254px;top:765px;width:312px;font-size:13.3px;line-height:26px;text-align:justify;letter-spacing:-.1px;color:var(--text-soft)}

.register{left:608px;top:690px;width:469px;height:278px;border-radius:8px;background:linear-gradient(var(--panel-top),var(--panel-bottom))}
.register-bow{left:608px;top:690px;width:110px;height:120px;background:linear-gradient(135deg,#c41a12,#e0473b);clip-path:polygon(0 0,100% 0,0 100%)}
.free-badge{left:990px;top:680px;width:72px;height:72px;border-radius:50%;background:var(--orange);border:4px solid var(--white);color:var(--white);font-family:"Oswald",sans-serif;font-size:20px;text-align:center;line-height:64px;transform:rotate(-12deg)}
.register-title{left:773px;top:710px;font-size:26px;font-weight:400;color:var(--red-title)}
.field-label{left:684px;font-size:19px;font-weight:300;color:var(--label)}
.field{left:827px;width:235px;height:28px;background:linear-gradient(#fff,#eef2f3);border:1px solid #e1e8ea}
.cta{left:862px;top:908px;width:139px;height:29px;border-radius:9px;background:linear-gradient(var(--orange-light),var(--orange));border:1px solid #b86200;color:#2a1800;font-size:18px;text-align:center;line-height:27px}
.optin{left:642px;top:984px;width:420px;font-size:13px;line-height:16px;color:var(--white);padding-left:22px}
.optin i{position:absolute;left:0;top:3px;width:13px;height:13px;background:#e8eeef;border:1px solid #999}
.members-arrow{left:903px;top:1013px}
.members-title{left:786px;top:1044px;font-family:"Anton",Impact,sans-serif;font-size:40px;color:#0d3c46;text-shadow:0 1px 0 #3c8a96;letter-spacing:.5px}

.site-footer{left:0;top:1111px;width:1087px;height:89px;background:var(--teal-deep)}
.copyright{left:29px;top:25px;font-size:13px;color:var(--footer-text)}
.social{top:40px;font-size:12px;color:var(--text-soft)}
.social b{display:inline-block;width:12px;height:12px;border-radius:50%;background:var(--teal-light);margin-right:5px;vertical-align:-1px}
</style>
</head>
<body>

<header class="site-header abs">
  <div class="brand abs">
    <span class="brand-mark"></span><span class="brand-name">splitguide</span>
    <div class="brand-tagline">taking it one step at a time</div>
  </div>
  <div class="search abs">
    <span>Search</span>
    <svg width="26" height="24" viewBox="0 0 26 24"><circle cx="10" cy="10" r="7" fill="none" stroke="#072f37" stroke-width="3"/><line x1="15" y1="15" x2="23" y2="22" stroke="#072f37" stroke-width="4" stroke-linecap="round"/></svg>
  </div>
</header>

<nav class="nav abs">
  <svg class="abs" width="1087" height="44" viewBox="0 0 1087 44" style="left:0;top:0">
    <defs><linearGradient id="ribbonFill" x1="0" y1="0" x2="0" y2="1"><stop offset="0" stop-color="#d02a12"/><stop offset="1" stop-color="#9a180a"/></linearGradient></defs>
    <polygon points="8,2 32,2 32,42 22,42 30,22" fill="var(--red-dark)"/>
    <polygon points="1079,2 1055,2 1055,42 1065,42 1057,22" fill="var(--red-dark)"/>
    <rect x="26" y="2" width="1035" height="40" fill="url(#ribbonFill)"/>
  </svg>
  <a class="active" href="#">About us</a>
  <a href="#" style="left:192px">Blog</a>
  <a href="#" style="left:261px">Forums</a>
  <a href="#" style="left:345px">Members area</a>
  <a href="#" style="left:465px">book reviews</a>
  <a href="#" style="left:578px">rivenmart affiliate marketing</a>
  <a href="#" style="left:786px">Shopping cart</a>
  <a href="#" style="left:910px">Contact us</a>
</nav>

<section class="hero abs">
  <div class="hero-devices abs" role="img" aria-label="E-readers with a green cover and a download button"></div>
  <div class="hero-reader abs" role="img" aria-label="Young man reading on a tablet"></div>
  <h1 class="hero-title abs">Lorem Ipsum is simply dummy text</h1>
  <p class="hero-text abs">standard dummy text ever since the 1500s, when an unknown printer took a galley of type and scrambled it to make a type specimen book. It has survived not only five centuries, but also the leap into electronic typesetting, remaining essentially unchanged.</p>
  <div class="dots abs"><i></i><i></i><i class="on"></i></div>
</section>
<div class="hero-shadow abs"></div>

<main>
  <h2 class="welcome-title abs">Welcome To Our Website</h2>
  <div class="survey-link abs">Answer a brief survey</div>
  <div class="ebook-cover abs" role="img" aria-label="Ebook cover"></div>
  <div class="new-badge abs">NEW</div>
  <p class="intro abs">Lorem Ipsum is simply dummy text of the printing and typesetting industry. Lorem Ipsum has been the industry's standard dummy text ever since the 1500s, when an unknown printer took a galley of type and scrambled it to make a type specimen book. It has survived not only five centuries, but also the leap into electronic typesetting, remaining essentially unchanged. It was popularised in the 1960s with the release of Lettrline sheets containing Lorem Ipsum passages, and more recently with desktop publishing software like Pagecraft Studio including versions of Lorem Ipsum.</p>

  <form class="register-form">
    <div class="register abs"></div>
    <div class="register-bow abs" role="img" aria-label="Red gift ribbon bow"></div>
    <div class="free-badge abs">FREE</div>
    <h3 class="register-title abs">Register Here</h3>
    <label class="field-label abs" style="top:775px">Username</label>
    <div class="field abs" style="top:774px"></div>
    <label class="field-label abs" style="top:818px">Email Address</label>
    <div class="field abs" style="top:818px"></div>
    <label class="field-label abs" style="top:862px">Phone Number</label>
    <div class="field abs" style="top:861px"></div>
    <div class="cta abs">Get it Now</div>
    <p class="optin abs"><i></i>Yes, make sure I don't miss out on more special offers and great free stuff!</p>
  </form>

  <svg class="members-arrow abs" width="54" height="28" viewBox="0 0 54 28"><polygon points="27,0 54,28 0,28" fill="#e6eef0"/></svg>
  <div class="members-title abs">MEMBERS AREA</div>
</main>

<footer class="site-footer abs">
  <div class="copyright abs">Copyright © 2011. www.splitguide.example</div>
  <span class="social abs" style="left:800px"><b></b>Friendly</span>
  <span class="social abs" style="left:870px"><b></b>Chirper</span>
  <span class="social abs" style="left:940px"><b></b>Searchly</span>
  <span class="social abs" style="left:1012px"><b></b>Feedline</span>
</footer>

</body>
</html>
```